Website - Corla Druvick

I need a website that has multiple pages and easy for me to update pictures, content and blogs as an ongoing basis’s.
It will have videos and needs to be compatible to view easily and aesthetically on mobile phones.
Please refer to this website for inspiration www.lorettaquisp.com

Coding

Coded - Design and coding required

Number of Pages Required

5+ page

Font styles to use
Other font styles liked:
• Refer to website provided as inspiration

Requirements
Must have
• Please use stock images for now to do design, but I will be providing all imagery, videos and content

```html
<!DOCTYPE html>
<html lang="en">
<head>
<meta charset="utf-8">
<title>Corla Druvick</title>
<link rel="stylesheet" href="https://fonts.googleapis.com/css2?family=Libre+Baskerville:wght@400;700&family=Lato:wght@400;700&display=swap">
<style>
:root{
  --ink:#1b1b1b;
  --white:#ffffff;
  --accent:#e8c49a;
  --nav-active:#e9c79e;
  --hero-dark:#141414;
  --cream:#f1eee0;
  --stone:#cdcbc4;
  --sand:#d3c49c;
  --sand-line:#e2d7b8;
}
*{box-sizing:border-box;margin:0;padding:0}
html,body{width:1200px;height:2954px;overflow:hidden}
body{font-family:"Libre Baskerville",Georgia,serif;color:var(--ink);background:var(--white);position:relative}
.abs{position:absolute}

/* hero */
.hero{left:0;top:0;width:1200px;height:738px;overflow:hidden;
  background:linear-gradient(100deg,#101010 0%,#232323 30%,#4a4e58 48%,#6b5548 62%,#a0765e 75%,#3a2a22 100%)}
.hero-photo{left:560px;top:0;width:640px;height:738px;
  background:radial-gradient(ellipse at 55% 55%,#c89a80 0%,#8a5e48 40%,rgba(40,28,22,0) 75%)}
.logo{left:75px;top:58px;font-size:42px;color:var(--white);letter-spacing:1px}
.nav{left:0;top:76px;width:1200px;font-size:15px;color:var(--white);text-transform:uppercase}
.nav a{position:absolute;color:inherit;text-decoration:none;white-space:nowrap}
.nav a.active{color:var(--nav-active);font-weight:700}
.hero-title{left:75px;top:300px;font-size:66px;font-weight:700;color:var(--white);letter-spacing:2px}
.hero-sub{left:75px;top:378px;width:520px;font-size:29px;line-height:42px;color:var(--white);letter-spacing:.5px}

/* about */
.about-photo{left:0;top:821px;width:440px;height:492px;background:linear-gradient(160deg,#3a2a22,#b98b72 45%,#d8ab92 60%,#4a3328)}
.about-circle{left:292px;top:920px;width:294px;height:294px;border-radius:50%;background:radial-gradient(circle at 55% 40%,#d8a888,#8a5a40 60%,#e8e4de 100%)}
.about-title{left:615px;top:855px;font-size:41px;line-height:50px}
.about-text{left:615px;top:977px;width:520px;font-family:"Lato",Arial,sans-serif;font-size:16.5px;line-height:34.3px;color:#333}
.btn{background:var(--accent);color:var(--ink);font-size:20px;display:flex;align-items:center;justify-content:center}
.about-btn{left:615px;top:1218px;width:187px;height:54px}

/* videos */
.videos{left:0;top:1389px;width:1200px;height:540px;background:var(--cream)}
.section-title{left:0;width:1200px;text-align:center;font-size:41px}
.video{top:1540px;width:513px;height:315px;display:flex;align-items:center;justify-content:center}
.video-a{left:75px;background:linear-gradient(180deg,#e6e4e0 0%,#c8c4c0 45%,#9a938c 100%)}
.video-b{left:614px;background:linear-gradient(180deg,#ebe9e6 0%,#b9b6b2 50%,#5d6170 100%)}

/* posts */
.posts{left:0;top:1929px;width:1200px;height:607px;background:var(--stone)}
.post-img{top:2086px;width:330px;height:245px}
.post-a{left:75px;background:linear-gradient(180deg,#d8d8d8,#6e6e6e 60%,#3a3a3a)}
.post-b{left:435px;background:linear-gradient(180deg,#3e4a40,#a87a5c 50%,#c49a80)}
.post-c{left:796px;background:linear-gradient(180deg,#b4c2cc,#5a6a78 45%,#d86aa8 75%,#6e6258)}
.post-title{top:2353px;width:330px;font-size:22px;line-height:31px}
.post-date{top:2428px;font-size:15px;font-weight:700;color:var(--white);letter-spacing:.5px}

/* signup */
.signup{left:0;top:2536px;width:1200px;height:321px;background:var(--sand)}
.signup-title{left:0;top:2590px;width:1200px;text-align:center;font-size:35px;line-height:46px;letter-spacing:.5px}
.signup-form{left:316px;top:2713px;width:568px;height:69px;background:var(--white)}
.signup-field{left:338px;top:2738px;font-size:15px}
.signup-btn{left:745px;top:2722px;width:131px;height:52px}

/* footer */
.footer{left:0;top:2857px;width:1200px;height:97px;background:var(--sand);border-top:1px solid var(--sand-line)}
.copyright{left:74px;top:2900px;font-family:"Lato",Arial,sans-serif;font-size:13px}
.social{left:900px;top:2898px;display:flex;gap:14px;font-family:"Lato",Arial,sans-serif;font-size:13px;font-weight:700;color:var(--ink)}
</style>
</head>
<body>

<section class="abs hero" role="img" aria-label="Close-up portrait photograph of Corla Druvick against a soft dark background"></section>
<div class="abs hero-photo" role="img" aria-label="Portrait photograph area"></div>
<div class="abs logo">Corla Druvick</div>
<nav class="abs nav">
  <a class="active" style="left:573px">Home</a>
  <a style="left:686px">About</a>
  <a style="left:806px">Blog</a>
  <a style="left:913px">Videos</a>
  <a style="left:1040px">Contact</a>
</nav>
<h1 class="abs hero-title">Corla Druvick</h1>
<p class="abs hero-sub">Miss Southern Star National Finalist 2021</p>

<div class="abs about-photo" role="img" aria-label="Portrait photograph of Corla Druvick"></div>
<div class="abs about-circle" role="img" aria-label="Smiling photograph of Corla Druvick in a circular frame"></div>
<h2 class="abs about-title" style="font-weight:400">About<br>Corla Druvick</h2>
<p class="abs about-text">Sed ut perspiciatis unde omnis iste natus error sit voluptatem accusantium doloremque laudantium, totam rem aperiam, eaque ipsa quae ab illo inventore veritatis et quasi architecto beatae vitae dicta sunt explicabo. Nemo enim ipsam voluptatem quia voluptas sit aspernatur aut odit aut fugit, sed quia consequuntur magni dolores eos qui ratione voluptatem.</p>
<div class="abs btn about-btn">Read More</div>

<section class="abs videos"></section>
<h2 class="abs section-title" style="top:1445px;font-weight:400">Videos</h2>
<div class="abs video video-a" role="img" aria-label="Video thumbnail: cooking in a white kitchen">
  <svg width="56" height="56" viewBox="0 0 56 56"><circle cx="28" cy="28" r="25" fill="none" stroke="#fff" stroke-width="4"/><path d="M22 16 L40 28 L22 40Z" fill="#fff"/></svg>
</div>
<div class="abs video video-b" role="img" aria-label="Video thumbnail: holding a teacup in a kitchen">
  <svg width="56" height="56" viewBox="0 0 56 56"><circle cx="28" cy="28" r="25" fill="none" stroke="#fff" stroke-width="4"/><path d="M22 16 L40 28 L22 40Z" fill="#fff"/></svg>
</div>

<section class="abs posts"></section>
<h2 class="abs section-title" style="top:2007px;font-weight:400">Latest Posts</h2>
<div class="abs post-img post-a" role="img" aria-label="Black and white photo by the water"></div>
<div class="abs post-img post-b" role="img" aria-label="Laughing photo with windswept hair"></div>
<div class="abs post-img post-c" role="img" aria-label="Photo in a pink dress on a jetty"></div>
<h3 class="abs post-title" style="left:75px;font-weight:400">Sed ut perspiciatis unde omnis magni</h3>
<h3 class="abs post-title" style="left:435px;font-weight:400">Sed ut perspiciatis unde omnis magni</h3>
<h3 class="abs post-title" style="left:796px;font-weight:400">Sed ut perspiciatis unde omnis magni</h3>
<div class="abs post-date" style="left:75px">Apr 23, 2021</div>
<div class="abs post-date" style="left:435px">Apr 23, 2021</div>
<div class="abs post-date" style="left:796px">Apr 23, 2021</div>

<section class="abs signup"></section>
<h2 class="abs signup-title" style="font-weight:400">Sign up with your email address to<br>receive news and updates.</h2>
<div class="abs signup-form"></div>
<div class="abs signup-field">Email Address</div>
<div class="abs btn signup-btn">Sign Up</div>

<footer class="abs footer"></footer>
<div class="abs copyright">Copyright © 2021 Company Name &nbsp;All Right Reserved</div>
<div class="abs social"><span>Kivo</span><span>Marlo</span><span>Pexa</span><span>Quill</span><span>Reelo</span></div>

</body>
</html>
```